Billboard for Post Frame Construction Company

We need a billboard designed for a post frame construction company.
The billboard needs to have:
enclosed red barn as base picture
Cedarline Custom Builders logo
Phone number (406) 555-0148
cedarlinebuilders.example
FREE QUOTE
Garages, Hobby Shops, Equestrian, Barndominiums, Commercial and more...
This billboard is scheduled to be in a rural part of Montana outside of Stevensvile, MT. The text must be legible on a highway.
Updates
Please do not add extra text that will make the billboard crowded or busy. The billboard is for a busy rural highway and the text needs to be visible. Thank you!
Requirements
Must have
- FREE QUOTE
Updated summer photo attached.
Nice to have
- Please use the updated summer photo for the billboard.
Please make sure the logo is prominent.
Should not have
- Extras that make the billboard too busy.
Do not add phone or web icons. Do not add the client tag line or anything extra. The client wants a simple billboard that is not busy and distracting.

```html
<!DOCTYPE html>
<html lang="en">
<head>
<meta charset="utf-8">
<title>Cedarline Custom Builders Billboard</title>
<link rel="stylesheet" href="https://fonts.googleapis.com/css2?family=Montserrat:wght@400;500;700;800&display=swap">
<style>
  :root {
    --brand-red: #c5202c;
    --brand-navy: #27347c;
    --logo-grey: #4b4b4d;
    --panel-white: #f4f4f5;
    --panel-grey: #e2e3e6;
    --stage: #e9eaec;
    --white: #ffffff;
  }
  * { margin: 0; padding: 0; box-sizing: border-box; }
  html, body {
    width: 1200px;
    height: 735px;
    overflow: hidden;
    background: var(--stage);
    font-family: "Montserrat", sans-serif;
  }
  .billboard {
    position: absolute;
    left: 0;
    top: 201px;
    width: 1200px;
    height: 332px;
    overflow: hidden;
    background: linear-gradient(135deg, var(--panel-white) 0%, var(--panel-grey) 55%, var(--panel-white) 100%);
  }
  .billboard__shapes {
    position: absolute;
    inset: 0;
    width: 1200px;
    height: 332px;
  }
  .web-address {
    position: absolute;
    left: 48px;
    top: 5px;
    width: 560px;
    color: var(--white);
    font-weight: 700;
    font-size: 19px;
    letter-spacing: 8.5px;
    line-height: 22px;
    white-space: nowrap;
  }
  .company-name {
    position: absolute;
    left: 38px;
    top: 112px;
    width: 440px;
    color: var(--logo-grey);
    font-weight: 500;
    text-align: center;
  }
  .company-name__primary {
    display: block;
    font-size: 58px;
    line-height: 62px;
    letter-spacing: 5px;
  }
  .company-name__secondary {
    display: block;
    font-size: 28px;
    line-height: 34px;
    letter-spacing: 2px;
  }
  .phone-number {
    position: absolute;
    left: 36px;
    top: 245px;
    color: var(--brand-navy);
    font-weight: 800;
    font-size: 51px;
    line-height: 60px;
    letter-spacing: -0.5px;
    white-space: nowrap;
  }
  .offer-band {
    position: absolute;
    left: 548px;
    top: 251px;
    height: 65px;
    display: flex;
    align-items: center;
    color: var(--white);
  }
  .offer-band__headline {
    font-weight: 800;
    font-size: 36px;
    letter-spacing: 0.5px;
    padding-right: 10px;
    border-right: 2px solid var(--white);
    line-height: 40px;
    white-space: nowrap;
  }
  .offer-band__services {
    padding-left: 8px;
    font-weight: 700;
    font-size: 15px;
    line-height: 18px;
    white-space: nowrap;
  }
</style>
</head>
<body>
  <main class="billboard">
    <svg class="billboard__shapes" viewBox="0 0 1200 332" aria-hidden="false">
      <defs>
        <linearGradient id="barn-photo-tones" x1="0" y1="0" x2="0" y2="1">
          <stop offset="0" stop-color="#d7dfe9"/>
          <stop offset="0.22" stop-color="#b9c4d1"/>
          <stop offset="0.38" stop-color="#c0363d"/>
          <stop offset="0.78" stop-color="#b3222b"/>
          <stop offset="0.9" stop-color="#cdbb9b"/>
          <stop offset="1" stop-color="#b9a582"/>
        </linearGradient>
      </defs>
      <!-- red top band and swoosh -->
      <rect class="top-band" x="0" y="12" width="640" height="30" fill="var(--brand-red)"/>
      <path class="swoosh" d="M592,0 L1200,0 L1200,332 L498,332 C462,200 500,70 592,0 Z" fill="var(--brand-red)"/>
      <!-- barn photo area -->
      <path class="barn-photo" role="img" aria-label="Photo of an enclosed red post frame barn with a white garage door, fencing and snowy mountains behind"
            d="M622,0 L1200,0 L1200,251 L512,251 C515,150 550,60 622,0 Z" fill="url(#barn-photo-tones)"/>
      <!-- offer band -->
      <path class="offer-band-shape" d="M512,251 L1200,251 L1200,316 L522,316 C517,295 513,273 512,251 Z" fill="var(--brand-navy)"/>
      <rect class="bottom-strip" x="540" y="316" width="660" height="16" fill="var(--white)"/>
    </svg>

    <p class="web-address">cedarlinebuilders.example</p>

    <h1 class="company-name">
      <span class="company-name__primary">CEDARLINE</span>
      <span class="company-name__secondary">CUSTOM BUILDERS</span>
    </h1>

    <p class="phone-number">(406) 555-0148</p>

    <div class="offer-band">
      <p class="offer-band__headline">FREE QUOTE</p>
      <p class="offer-band__services">Garages, Hobby Shops, Equestrian,<br>Barndominiums, Commercial and more...</p>
    </div>
  </main>
</body>
</html>
```